Small law practice looking for logo, letterhead, and business card design

I need a logo, letterhead, and business card for a small law practice. Basically it's just me, my paralegal, and my private investigator. We do primarily criminal defense, both trial and appeal, in state and federal court. We work mostly in complex cases, and serious crimes. We don't handle DUI, or volume business. Think more like major drug crimes, murder, etc. Because of this we do a limited number of cases each year. We're picky because we do big cases, and take the time to focus on them and do them right.

The office is in an old rennovated building in Elmgrove, Westmont, with lots of 1920's wood and glass, looks vaguely Cedric Willoughby. Interior is decorated with comic and pulp art, some antiques, and some funky stuff. I'm looking for something classy, timeless, and understated, but unique. My name is Tobias Weller, I suppose that would be useful information, since my name is on the door.

I want a logo and theme that can translate across business cards, letterhead, email footers, and website.

```html
<!DOCTYPE html>
<html lang="en">
<head>
<meta charset="utf-8">
<title>Tobias Weller Law Office – Business Cards</title>
<link rel="stylesheet" href="https://fonts.googleapis.com/css2?family=Righteous&family=Oswald:wght@700&family=Cormorant+Garamond:wght@500&display=swap">
<style>
  :root {
    --cream: #fffcc8;
    --shade-mid: #cfc9a0;
    --shade-dark: #6b6552;
    --ink: #1d1a14;
    --edge: #5a5750;
  }
  html, body {
    margin: 0;
    padding: 0;
    overflow: hidden;
    background: var(--cream);
  }
  .canvas {
    position: relative;
    width: 1200px;
    height: 997px;
    background: var(--cream);
    border: 1px solid #9a988e;
    box-sizing: border-box;
    overflow: hidden;
  }
  .backdrop-swoosh, .card-swoosh {
    position: absolute;
    inset: 0;
    width: 100%;
    height: 100%;
  }
  .card {
    position: absolute;
    width: 790px;
    height: 481px;
    background: var(--cream);
    border: 1px solid var(--edge);
    box-sizing: border-box;
    overflow: hidden;
    color: var(--ink);
    font-family: "Cormorant Garamond", Georgia, serif;
    font-weight: 500;
  }
  .card--first { left: 34px; top: 35px; }
  .card--second { left: 362px; top: 481px; width: 792px; }
  .card > * { position: absolute; margin: 0; white-space: nowrap; }
  .firm-name {
    left: 40px;
    line-height: 1;
  }
  .card--first .firm-name {
    top: 50px;
    font-family: "Righteous", "Arial Black", sans-serif;
    font-size: 42px;
    letter-spacing: 3px;
  }
  .card--second .firm-name {
    top: 50px;
    left: 34px;
    font-family: "Oswald", "Arial Narrow", sans-serif;
    font-weight: 700;
    font-size: 54px;
    letter-spacing: 0;
  }
  .rule {
    height: 3px;
    background: var(--ink);
  }
  .card--first .rule { left: 40px; top: 91px; width: 728px; }
  .card--second .rule { left: 29px; top: 121px; width: 728px; }
  .firm-tagline { font-size: 30px; line-height: 1; }
  .card--first .firm-tagline { left: 240px; top: 100px; }
  .card--second .firm-tagline { left: 220px; top: 131px; }
  .card-heading { font-size: 48px; line-height: 1; }
  .card--first .card-heading { left: 64px; top: 224px; }
  .card--second .card-heading { left: 59px; top: 262px; }
  .contact-line { font-size: 24px; line-height: 1; }
  .card--first .contact-address { left: 65px; top: 294px; }
  .card--first .contact-tel { left: 65px; top: 334px; }
  .card--second .contact-address { left: 59px; top: 329px; }
  .card--second .contact-tel { left: 59px; top: 369px; }
  .leader { letter-spacing: -0.5px; font-size: 16px; }
</style>
</head>
<body>
<main class="canvas">
  <svg class="backdrop-swoosh" viewBox="0 0 1200 997" preserveAspectRatio="none" aria-hidden="true">
    <defs>
      <linearGradient id="backdropShade" x1="0.55" y1="0.45" x2="1" y2="1">
        <stop offset="0" stop-color="var(--cream)"/>
        <stop offset="0.5" stop-color="var(--shade-mid)"/>
        <stop offset="1" stop-color="var(--shade-dark)"/>
      </linearGradient>
    </defs>
    <path d="M1200 170 C1150 300 1080 420 960 520 C700 700 300 720 80 760 C30 800 10 900 0 997 L1200 997 Z" fill="url(#backdropShade)"/>
  </svg>

  <section class="card card--first" aria-label="Business card, first version">
    <svg class="card-swoosh" viewBox="0 0 790 481" preserveAspectRatio="none" aria-hidden="true">
      <defs>
        <linearGradient id="cardShadeA" x1="0.3" y1="0.55" x2="1" y2="1">
          <stop offset="0" stop-color="var(--cream)"/>
          <stop offset="0.45" stop-color="#e3ddb2"/>
          <stop offset="1" stop-color="#8a846c"/>
        </linearGradient>
      </defs>
      <path d="M790 10 C770 200 650 280 380 280 C250 282 120 380 0 470 L0 481 L790 481 Z" fill="url(#cardShadeA)"/>
    </svg>
    <h1 class="firm-name">Tobias Weller</h1>
    <div class="rule"></div>
    <p class="firm-tagline">Law Office</p>
    <p class="card-heading">Tobias Weller</p>
    <p class="contact-line contact-address">Address<span class="leader">..........................................</span></p>
    <p class="contact-line contact-tel">tel<span class="leader">.......................................................</span></p>
  </section>

  <section class="card card--second" aria-label="Business card, second version">
    <svg class="card-swoosh" viewBox="0 0 792 481" preserveAspectRatio="none" aria-hidden="true">
      <defs>
        <linearGradient id="cardShadeB" x1="0.3" y1="0.55" x2="1" y2="1">
          <stop offset="0" stop-color="var(--cream)"/>
          <stop offset="0.45" stop-color="#e3ddb2"/>
          <stop offset="1" stop-color="#7d7760"/>
        </linearGradient>
      </defs>
      <path d="M792 10 C772 200 650 278 380 278 C250 280 120 380 0 470 L0 481 L792 481 Z" fill="url(#cardShadeB)"/>
    </svg>
    <h2 class="firm-name">Tobias Weller</h2>
    <div class="rule"></div>
    <p class="firm-tagline">Law Office</p>
    <p class="card-heading">Elmgrove, Westmont</p>
    <p class="contact-line contact-address">Address<span class="leader">..........................................</span></p>
    <p class="contact-line contact-tel">tel<span class="leader">.......................................................</span></p>
  </section>
</main>
</body>
</html>
```